Online medical reviews website needs banner advert!

We need banner advert templates for our website, www.traineepanel.net. These should meet the technical requirements of our partner (uploaded).

Our groundbreaking website allows doctors in training to rate and review their training.

The adverts should use the same modern design language and colour scheme as our website. They should use the text 'Help a junior doctor make a big decision - rate your training!'.

Vector assets should be supplied, allowing us to use alternative text in future.
Updates

Industry/Entity Type

Healthcare

Font styles to use
Other font styles liked:
• Karla

Colors
3277b5
0555a3
ffffff

Requirements
Must have
• Similar design to our website. Should be elegant & modern. Must allow future text to be easily inserted.
Should not have
• Unrelated design.

```html
<!DOCTYPE html>
<html lang="en">
<head>
<meta charset="utf-8">
<title>Trainee Panel – Banner Templates</title>
<link href="https://fonts.googleapis.com/css2?family=Karla:wght@500;700&display=swap" rel="stylesheet">
<style>
  :root {
    --canvas: #bcbdbf;
    --label: #1a1a1a;
    --white: #ffffff;
    --brand-blue: #0555a3;
    --photo-dark: #2a2a2c;
    --photo-mid: #5a5b5e;
    --rule: rgba(255,255,255,0.9);
  }
  * { margin: 0; padding: 0; box-sizing: border-box; }
  html, body { width: 1200px; height: 1000px; overflow: hidden; }
  body {
    position: relative;
    background: var(--canvas);
    font-family: "Karla", Arial, sans-serif;
  }
  .size-label {
    position: absolute;
    font-family: "Karla", Arial, sans-serif;
    font-weight: 700;
    font-size: 24px;
    color: var(--label);
    letter-spacing: 0.5px;
    line-height: 1;
  }
  .banner { position: absolute; overflow: hidden; background: var(--white); }
  .banner-photo {
    position: absolute;
    background: linear-gradient(160deg, var(--photo-mid) 0%, #3b3c3f 45%, var(--photo-dark) 100%);
  }
  .brand-name {
    position: absolute;
    color: var(--white);
    font-weight: 500;
    letter-spacing: -0.5px;
    white-space: nowrap;
    line-height: 1;
  }
  .rule { position: absolute; background: var(--rule); }
  .headline {
    position: absolute;
    color: var(--white);
    font-weight: 500;
    white-space: nowrap;
  }
  .cta {
    position: absolute;
    color: var(--brand-blue);
    font-weight: 500;
    white-space: nowrap;
  }
  .chevron { position: absolute; }
  .chevron path { fill: none; stroke: var(--brand-blue); stroke-width: 2; }
</style>
</head>
<body>

<!-- 300 x 600 skyscraper -->
<div class="size-label" style="left:125px; top:74px;">300 x 600</div>
<section class="banner" style="left:67px; top:111px; width:274px; height:548px;">
  <div class="banner-photo" role="img" aria-label="Black and white photo of junior doctors holding large balloon letters outside a building" style="left:0; top:0; width:274px; height:404px;"></div>
  <div class="brand-name" style="left:23px; top:56px; font-size:20px;">Trainee Panel</div>
  <div class="rule" style="left:23px; top:115px; width:170px; height:2px;"></div>
  <p class="headline" style="left:26px; top:148px; font-size:26px; line-height:44.5px; letter-spacing:2.2px;">Help a<br>junior doctor<br>make a big<br>decision...</p>
  <div class="rule" style="left:23px; top:359px; width:170px; height:2px;"></div>
  <p class="cta" style="left:23px; top:440px; font-size:22px; line-height:30px; letter-spacing:2.4px;">Rate your<br>training</p>
  <svg class="chevron" style="left:219px; top:451px;" width="20" height="36" viewBox="0 0 20 36"><path d="M2 1 L18 18 L2 35"/></svg>
</section>

<!-- 300 x 250 medium rectangle -->
<div class="size-label" style="left:512px; top:74px;">300 x 250</div>
<section class="banner" style="left:395px; top:111px; width:383px; height:319px;">
  <div class="banner-photo" role="img" aria-label="Black and white photo of junior doctors with balloon letters in a street" style="left:0; top:0; width:383px; height:249px;"></div>
  <div class="brand-name" style="left:43px; top:40px; font-size:25px;">Trainee Panel</div>
  <div class="rule" style="left:43px; top:90px; width:202px; height:2px;"></div>
  <p class="headline" style="left:44px; top:108px; font-size:24px; line-height:43px; letter-spacing:1.4px;">Help a junior doctor<br>make a big decision...</p>
  <div class="rule" style="left:43px; top:211px; width:202px; height:1px;"></div>
  <p class="cta" style="left:42px; top:266px; font-size:22px; line-height:30px; letter-spacing:1.8px;">Rate your training</p>
  <svg class="chevron" style="left:320px; top:269px;" width="18" height="28" viewBox="0 0 18 28"><path d="M2 1 L15 14 L2 27"/></svg>
</section>

<!-- 728 x 90 leaderboard -->
<div class="size-label" style="left:410px; top:501px;">728 x 90</div>
<section class="banner" style="left:395px; top:543px; width:752px; height:93px;">
  <div class="banner-photo" role="img" aria-label="Black and white photo of a group of junior doctors outdoors" style="left:0; top:0; width:563px; height:93px;"></div>
  <div class="brand-name" style="left:15px; top:39px; font-size:16px;">Trainee Panel</div>
  <div class="rule" style="left:172px; top:18px; width:1px; height:58px;"></div>
  <p class="headline" style="left:204px; top:16px; font-size:22px; line-height:30px; letter-spacing:2.3px;">Help a junior doctor<br>make a big decision...</p>
  <p class="cta" style="left:584px; top:25px; font-size:18px; line-height:22px; letter-spacing:1.8px;">Rate your<br>training</p>
  <svg class="chevron" style="left:706px; top:32px;" width="18" height="30" viewBox="0 0 18 30"><path d="M2 1 L15 15 L2 29"/></svg>
</section>

<!-- 970 x 90 billboard -->
<section class="banner" style="left:67px; top:722px; width:1016px; height:94px;">
  <div class="banner-photo" role="img" aria-label="Black and white photo of junior doctors gathered in front of railings" style="left:0; top:0; width:784px; height:94px;"></div>
  <div class="brand-name" style="left:27px; top:36px; font-size:28px;">Trainee Panel</div>
  <div class="rule" style="left:297px; top:19px; width:1px; height:59px;"></div>
  <p class="headline" style="left:343px; top:15px; font-size:26px; line-height:31px; letter-spacing:3px;">Help a junior doctor<br>make a big decision...</p>
  <p class="cta" style="left:811px; top:18px; font-size:22px; line-height:28px; letter-spacing:2.6px;">Rate your<br>training</p>
  <svg class="chevron" style="left:960px; top:33px;" width="18" height="30" viewBox="0 0 18 30"><path d="M2 1 L15 15 L2 29"/></svg>
</section>
<div class="size-label" style="left:88px; top:838px;">970 x 90</div>

</body>
</html>
```